Simple and clean

We need a business card design for a new company called Estate Lantern. It is a search engine to find current properties for sale or rent in New Zealand market.
We have already a colour scheme that we would like people to use.
Light brown: #D4CCB0
Light green: #D6E4D4
Green: #669966
Black/White
It is OK to divert from this colour scheme slightly as long as there is a green component to the business card.
Final design should be clean, simple and should communicate the nature of the business.
Target Market(s)
- First home buyers
- Real estate agents
- People seeking rentals
Industry/Entity Type
Business
Requirements
Must have
- Use those or similar colours.
Light brown: #D4CCB0
Light green: #D6E4D4
Green: #669966
Black/White

```html
<!DOCTYPE html>
<html lang="en">
<head>
<meta charset="utf-8">
<title>Estate Lantern – Business Card</title>
<link rel="stylesheet" href="https://fonts.googleapis.com/css2?family=Arimo:wght@700&display=swap">
<style>
  :root {
    --page-bg: #ececec;
    --card-bg: #ffffff;
    --card-edge: #d9d9d9;
    --green: #5b8c5b;
    --green-dark: #4c7a4c;
    --black: #111111;
  }
  * { margin: 0; padding: 0; box-sizing: border-box; }
  html, body {
    width: 1200px;
    height: 899px;
    overflow: hidden;
    background: var(--page-bg);
  }
  .card {
    position: absolute;
    left: 120px;
    top: 175px;
    width: 960px;
    height: 550px;
    background: var(--card-bg);
    border: 1px solid var(--card-edge);
    font-family: "Arimo", Arial, sans-serif;
    font-weight: 700;
  }
  .brand-name {
    position: absolute;
    left: 40px;
    top: 240px;
    transform: translate(-50%, -50%) rotate(-90deg);
    white-space: nowrap;
    font-size: 44px;
    letter-spacing: -1px;
    color: var(--black);
  }
  .contact {
    position: absolute;
    left: 60px;
    right: 0;
    top: 0;
    text-align: center;
    color: var(--green);
  }
  .contact p { position: absolute; left: 0; right: 0; line-height: 1; }
  .person-name { top: 130px; font-size: 56px; letter-spacing: -0.5px; color: var(--green-dark); }
  .person-role { top: 198px; font-size: 32px; }
  .phone { top: 258px; font-size: 36px; }
  .email { top: 314px; font-size: 34px; letter-spacing: -0.5px; }
  .website { top: 444px; font-size: 36px; letter-spacing: -0.5px; color: var(--green-dark); }
</style>
</head>
<body>
  <div class="card">
    <div class="brand-name">Estate Lantern</div>
    <div class="contact">
      <p class="person-name">Mara Quinlan</p>
      <p class="person-role">Director</p>
      <p class="phone">000 000 000</p>
      <p class="email">mara.quinlan@estatelantern.co.nz</p>
      <p class="website">www.estatelantern.co.nz</p>
    </div>
  </div>
</body>
</html>
```